Trucking company needs business card design

New trucking company needs fresh ideas on a business card. Contracted exclusively to ParcelWing, can incorporate their colors or style, but not necessary.
Calder Haulage, Inc (with or without the Inc.)
Dale Whitcombe, CEO
801-555-0147
PO BOX 372
Brookvale, UT
Updates

Need to add my email address to the card--calderhaulageinc@roadmail.example

Industry/Entity Type

Trucking Company

```html
<!DOCTYPE html>
<html lang="en">
<head>
<meta charset="utf-8">
<title>Calder Haulage – Business Cards</title>
<link href="https://fonts.googleapis.com/css2?family=Saira:wght@400;500;700&display=swap" rel="stylesheet">
<style>
  :root {
    --stage: #cbcbcb;
    --purple: #622d8b;
    --green: #44b54a;
    --paper: #f2f2f2;
    --ink: #1b1b1b;
    --white: #f4f4f4;
    --rule: #8a8a8a;
  }
  * { box-sizing: border-box; margin: 0; padding: 0; }
  html, body { width: 1148px; height: 1200px; overflow: hidden; }
  body { background: var(--stage); font-family: "Saira", sans-serif; position: relative; }

  .card {
    position: absolute; width: 515px; height: 293px;
    display: flex; align-items: center; justify-content: center;
  }
  .col-left { left: 50px; }
  .col-right { left: 583px; }
  .row-1 { top: 148px; }
  .row-2 { top: 456px; }
  .row-3 { top: 763px; }

  .card--purple { background: var(--purple); }
  .card--green { background: var(--green); }
  .card--paper { background: var(--paper); }
  .card--black { background: var(--ink); }

  .wordmark {
    display: flex; align-items: center; gap: 8px;
    font-weight: 700; color: var(--purple); line-height: 1;
  }
  .wordmark__square { width: 12px; height: 12px; background: currentColor; flex: none; }
  .wordmark__text { display: flex; flex-direction: column; }
  .wordmark__primary { font-size: 42px; letter-spacing: 1px; }
  .wordmark__secondary { font-size: 14px; letter-spacing: 9.4px; margin-top: 2px; }
  .wordmark--white { color: var(--white); }
  .wordmark--small .wordmark__primary { font-size: 30px; letter-spacing: 0.5px; }
  .wordmark--small .wordmark__secondary { font-size: 10px; letter-spacing: 6.5px; }
  .wordmark--small .wordmark__square { width: 9px; height: 9px; }

  .card--back { justify-content: flex-start; }
  .card--back .wordmark { position: absolute; left: 34px; top: 118px; }
  .divider { position: absolute; left: 239px; top: 94px; width: 1px; height: 103px; background: var(--rule); }
  .details { position: absolute; left: 270px; top: 96px; font-size: 13px; line-height: 14px; }
  .details__group { position: relative; padding-left: 10px; margin-bottom: 10px; }
  .details__group::before {
    content: ""; position: absolute; left: 0; top: 3px;
    border-left: 5px solid var(--green);
    border-top: 3.5px solid transparent; border-bottom: 3.5px solid transparent;
  }
  .details__name { font-size: 16px; font-weight: 700; color: var(--purple); line-height: 16px; }
  .details--green .details__line { color: var(--green); }
  .details--ink .details__line { color: var(--ink); }
</style>
</head>
<body>
  <section class="card card--purple col-left row-1">
    <div class="wordmark wordmark--white">
      <span class="wordmark__square"></span>
      <span class="wordmark__text"><span class="wordmark__primary">CALDER</span><span class="wordmark__secondary">HAULAGE</span></span>
    </div>
  </section>

  <section class="card card--green col-right row-1">
    <div class="wordmark">
      <span class="wordmark__square"></span>
      <span class="wordmark__text"><span class="wordmark__primary">CALDER</span><span class="wordmark__secondary">HAULAGE</span></span>
    </div>
  </section>

  <section class="card card--paper col-left row-2">
    <div class="wordmark">
      <span class="wordmark__square"></span>
      <span class="wordmark__text"><span class="wordmark__primary">CALDER</span><span class="wordmark__secondary">HAULAGE</span></span>
    </div>
  </section>

  <section class="card card--black col-right row-2">
    <div class="wordmark">
      <span class="wordmark__square"></span>
      <span class="wordmark__text"><span class="wordmark__primary">CALDER</span><span class="wordmark__secondary">HAULAGE</span></span>
    </div>
  </section>

  <section class="card card--paper card--back col-left row-3">
    <div class="wordmark wordmark--small">
      <span class="wordmark__square"></span>
      <span class="wordmark__text"><span class="wordmark__primary">CALDER</span><span class="wordmark__secondary">HAULAGE</span></span>
    </div>
    <span class="divider"></span>
    <div class="details details--green">
      <div class="details__group"><div class="details__name">DALE WHITCOMBE</div><div class="details__line">CEO</div></div>
      <div class="details__group"><div class="details__line">801.555.0147</div><div class="details__line">calderhaulageinc@roadmail.example</div></div>
      <div class="details__group"><div class="details__line">PO BOX 372</div><div class="details__line">Brookvale, UT</div></div>
    </div>
  </section>

  <section class="card card--paper card--back col-right row-3">
    <div class="wordmark wordmark--small">
      <span class="wordmark__square"></span>
      <span class="wordmark__text"><span class="wordmark__primary">CALDER</span><span class="wordmark__secondary">HAULAGE</span></span>
    </div>
    <span class="divider"></span>
    <div class="details details--ink">
      <div class="details__group"><div class="details__name">DALE WHITCOMBE</div><div class="details__line">CEO</div></div>
      <div class="details__group"><div class="details__line">801.555.0147</div><div class="details__line">calderhaulageinc@roadmail.example</div></div>
      <div class="details__group"><div class="details__line">PO BOX 372</div><div class="details__line">Brookvale, UT</div></div>
    </div>
  </section>
</body>
</html>
```